Business Cards

Business card design for my company.
I would like the card's background colour to be black. You can also see our web site to get an idea of our brand. https://www.dlqmarrowfield.com.au/
- Name
- Email

```html
<!DOCTYPE html>
<html lang="en">
<head>
<meta charset="utf-8">
<title>DLQ Marrowfield – Business Cards</title>
<link rel="stylesheet" href="https://fonts.googleapis.com/css2?family=Saira:wght@600;700&family=Crimson+Pro:wght@500&display=swap">
<style>
  :root {
    --page-bg: #e6e6e6;
    --card-black: #000000;
    --card-white: #ffffff;
    --brand-green: #0b9444;
    --brand-green-dark: #067a35;
    --icon-navy: #23283a;
    --text-dark: #1b1b1b;
    --logo-white: #f2f2f2;
  }
  * { margin: 0; padding: 0; box-sizing: border-box; }
  html, body {
    width: 1200px; height: 849px; overflow: hidden;
    background: var(--page-bg);
  }
  .sheet {
    width: 1200px; height: 849px;
    display: flex; flex-direction: column;
    align-items: center; justify-content: center;
    gap: 50px;
  }
  .card {
    position: relative;
    width: 600px; height: 343px;
    overflow: hidden;
  }
  .card--back { background: var(--card-black); }
  .card--front { background: var(--card-white); }
  .card__corners {
    position: absolute; inset: 0;
    width: 100%; height: 100%;
  }
  .brand-name {
    position: absolute; inset: 0;
    display: flex; align-items: center; justify-content: center;
    font-family: "Saira", sans-serif;
    font-weight: 700;
    font-size: 46px;
    letter-spacing: 2px;
    color: var(--logo-white);
  }
  .person {
    position: absolute; left: 56px; top: 76px;
  }
  .person__name {
    font-family: "Saira", sans-serif;
    font-weight: 700;
    font-size: 27px;
    line-height: 1;
    color: var(--brand-green);
    border-bottom: 2px solid var(--brand-green);
    padding-bottom: 1px;
    display: inline-block;
  }
  .person__title {
    font-family: "Saira", sans-serif;
    font-weight: 600;
    font-size: 13px;
    color: var(--brand-green);
    margin-top: 2px;
  }
  .contacts {
    position: absolute; left: 85px; top: 146px;
    list-style: none;
  }
  .contacts__item {
    display: flex; align-items: center;
    height: 28px; margin-bottom: 12px;
    font-family: "Crimson Pro", serif;
    font-weight: 500;
    font-size: 18px;
    color: var(--text-dark);
  }
  .contacts__icon {
    width: 28px; height: 28px; flex: none;
    margin-right: 12px;
  }
</style>
</head>
<body>
<main class="sheet">

  <section class="card card--back">
    <svg class="card__corners" viewBox="0 0 600 343" aria-hidden="true">
      <path d="M0 0H106A106 106 0 0 0 0 106Z" fill="var(--brand-green-dark)"/>
      <path d="M0 0H106A114 114 0 0 0 0 98Z" fill="var(--brand-green)"/>
      <path d="M600 343H494A106 106 0 0 0 600 237Z" fill="var(--brand-green-dark)"/>
      <path d="M600 343H494A114 114 0 0 0 600 245Z" fill="var(--brand-green)"/>
    </svg>
    <div class="brand-name">DLQ MARROWFIELD</div>
  </section>

  <section class="card card--front">
    <svg class="card__corners" viewBox="0 0 600 343" aria-hidden="true">
      <path d="M0 0H106A106 106 0 0 0 0 106Z" fill="var(--brand-green-dark)"/>
      <path d="M0 0H106A114 114 0 0 0 0 98Z" fill="var(--brand-green)"/>
      <path d="M600 343H494A106 106 0 0 0 600 237Z" fill="var(--brand-green-dark)"/>
      <path d="M600 343H494A114 114 0 0 0 600 245Z" fill="var(--brand-green)"/>
    </svg>

    <div class="person">
      <div class="person__name">Tom Ashcroft</div>
      <div class="person__title">General Manager</div>
    </div>

    <ul class="contacts">
      <li class="contacts__item">
        <svg class="contacts__icon" viewBox="0 0 28 28" aria-hidden="true">
          <circle cx="14" cy="14" r="14" fill="var(--icon-navy)"/>
          <path d="M10 8.5c.6-.5 1.3-.4 1.7.2l1.2 1.8c.3.5.2 1.1-.2 1.5l-.8.7c.6 1.4 1.6 2.5 3 3.2l.7-.8c.4-.4 1-.5 1.5-.2l1.8 1.1c.6.4.7 1.2.2 1.7l-.9.9c-.8.8-2 .9-3 .4-3-1.5-5.1-3.7-6.4-6.6-.4-1-.3-2.1.4-2.9Z" fill="#fff"/>
        </svg>
        0400 555 018
      </li>
      <li class="contacts__item">
        <svg class="contacts__icon" viewBox="0 0 28 28" aria-hidden="true">
          <circle cx="14" cy="14" r="14" fill="var(--icon-navy)"/>
          <rect x="8" y="10" width="12" height="8.5" fill="none" stroke="#fff" stroke-width="1.2"/>
          <path d="M8 10l6 5 6-5M8 18.5l4.5-4.2M20 18.5l-4.5-4.2" fill="none" stroke="#fff" stroke-width="1.1"/>
        </svg>
        info@dlqmarrowfield.com.au
      </li>
      <li class="contacts__item">
        <svg class="contacts__icon" viewBox="0 0 28 28" aria-hidden="true">
          <circle cx="14" cy="14" r="14" fill="var(--icon-navy)"/>
          <g fill="none" stroke="#fff" stroke-width="1.1">
            <circle cx="14" cy="14" r="6.5"/>
            <ellipse cx="14" cy="14" rx="2.8" ry="6.5"/>
            <path d="M7.5 14h13M8.5 10.8h11M8.5 17.2h11"/>
          </g>
        </svg>
        dlqmarrowfield.com.au
      </li>
      <li class="contacts__item">
        <svg class="contacts__icon" viewBox="0 0 28 28" aria-hidden="true">
          <circle cx="14" cy="14" r="14" fill="var(--icon-navy)"/>
          <path d="M14 21.5s-5-5.2-5-8.6a5 5 0 0 1 10 0c0 3.4-5 8.6-5 8.6Z" fill="#fff"/>
          <circle cx="14" cy="12.8" r="1.9" fill="var(--icon-navy)"/>
        </svg>
        Northvale, Tasmania, Australia
      </li>
    </ul>
  </section>

</main>
</body>
</html>
```